Intelligent design image for our website

I would like an awesome image for our website that showcases the intelligent design of our app. We currently have a test web site here.
https://www.roadpliant.com.au/test-ewd/
I really do not like the graphic next to the "Intelligent design" and i want something much better than this.
Our app is used by Australian Truck Drivers. It would be nice to have a little bit of an Australian feel, but most importantly is should clearly showcase our app look a feel and the screens should be as legible (readable) as possible. These examples could be used for inspiration.
https://mockvendra.net/products/free-app-showcase-mockup-psd-5817402
https://www.plontrix.com/community/file/2294618830157362901/AppScreen-Intro-Page-Layout-for-Phone-Apps-Display

```html
<!DOCTYPE html>
<html lang="en">
<head>
<meta charset="utf-8">
<title>Roadpliant EWD – Report Transfer</title>
<link rel="stylesheet" href="https://fonts.googleapis.com/css2?family=Lato:wght@400;700&display=swap">
<style>
  :root{
    --bg:#ffffff;
    --ring:#d6ecd1;
    --ink:#2b2b2b;
    --muted:#8a8a8a;
    --rule:#e9e9e9;
    --sync:#2b9fd8;
    --ok:#3cb24a;
    --btn-dark:#222222;
    --bezel:#111111;
  }
  *{box-sizing:border-box;margin:0;padding:0}
  html,body{width:1156px;height:1200px;overflow:hidden;background:var(--bg)}
  body{font-family:"Lato",sans-serif;color:var(--ink);position:relative}
  .rings{position:absolute;left:0;top:0;width:1156px;height:1200px}
  .phone-frame{position:absolute;left:153px;top:125px;width:463px;height:938px;background:var(--bezel);border-radius:62px;box-shadow:inset 0 0 0 3px #3a3a3a}
  .side-key{position:absolute;width:4px;background:var(--bezel);border-radius:2px}
  .screen{position:absolute;left:175px;top:145px;width:418px;height:898px;background:#fff;border-radius:42px;overflow:hidden}
  .notch{position:absolute;left:97px;top:-1px;width:233px;height:33px;background:var(--bezel);border-radius:0 0 22px 22px}
  .abs{position:absolute;white-space:nowrap;line-height:1}
  .status-time{left:19px;top:16px;font-size:17px;font-weight:700}
  .status-arrow{left:58px;top:18px}
  .status-icons{right:14px;top:17px}
  .back{left:18px;top:72px}
  .driver-name{left:61px;top:60px;font-size:16px;font-weight:700}
  .driver-license{left:61px;top:89px;font-size:13px;color:var(--muted)}
  .sync-ok{left:370px;top:62px}
  .sync-btn{left:343px;top:86px;width:72px;height:22px;background:var(--sync);color:#fff;font-size:11px;border-radius:3px;display:flex;align-items:center;justify-content:center}
  .rule{position:absolute;left:0;right:0;height:1px;background:var(--rule)}
  .page-title{left:14px;top:132px;font-size:18px;font-weight:700}
  .field-label{left:14px;font-size:11px;color:#555}
  .field-value{left:14px;font-size:17px}
  .field-line{position:absolute;left:14px;width:391px;height:1px;background:var(--rule)}
  .email{color:var(--muted)}
  .subject{font-weight:700}
  .body-text{left:19px;top:369px;font-size:17px;font-weight:700;line-height:20px;white-space:normal;width:345px}
  .body-text p{margin-bottom:20px}
  .count{right:13px;top:626px;font-size:12px;color:#c4c4c4}
  .btn{position:absolute;top:833px;height:47px;width:185px;border-radius:6px;display:flex;align-items:center;justify-content:center;font-size:16px;font-weight:700}
  .btn-return{left:14px;border:1.5px solid #bdbdbd;color:var(--ink)}
  .btn-send{left:220px;background:var(--btn-dark);color:#fff}
</style>
</head>
<body>
  <svg class="rings" viewBox="0 0 1156 1200" aria-hidden="true">
    <defs>
      <filter id="ringBlur" x="-50%" y="-50%" width="200%" height="200%"><feGaussianBlur stdDeviation="14"/></filter>
    </defs>
    <g fill="none" stroke="var(--ring)" filter="url(#ringBlur)">
      <circle cx="382" cy="599" r="278" stroke-width="44"/>
      <circle cx="382" cy="599" r="408" stroke-width="48"/>
      <circle cx="382" cy="599" r="535" stroke-width="52"/>
    </g>
  </svg>

  <div class="phone-frame" aria-hidden="true"></div>
  <div class="side-key" style="left:150px;top:252px;height:32px"></div>
  <div class="side-key" style="left:150px;top:318px;height:70px"></div>
  <div class="side-key" style="left:150px;top:405px;height:70px"></div>
  <div class="side-key" style="left:614px;top:340px;height:110px"></div>

  <main class="screen">
    <div class="notch" aria-hidden="true">
      <svg width="233" height="33" viewBox="0 0 233 33">
        <circle cx="17" cy="14" r="6" fill="#2a2a2a"/><circle cx="62" cy="14" r="7" fill="#555"/>
        <rect x="82" y="11" width="56" height="6" rx="3" fill="#2e2e2e"/>
        <circle cx="162" cy="14" r="6" fill="#2a2a2a"/><circle cx="207" cy="14" r="7" fill="#222"/>
      </svg>
    </div>
    <span class="abs status-time">8:53</span>
    <svg class="abs status-arrow" width="13" height="13" viewBox="0 0 13 13" aria-hidden="true"><path d="M12 1 1 6l5 1 1 5z" fill="#333"/></svg>
    <svg class="abs status-icons" width="72" height="14" viewBox="0 0 72 14" aria-hidden="true">
      <rect x="0" y="9" width="3" height="4" fill="#333"/><rect x="5" y="6" width="3" height="7" fill="#333"/><rect x="10" y="3" width="3" height="10" fill="#bbb"/>
      <path d="M22 5a10 10 0 0 1 14 0M25 8a6 6 0 0 1 8 0" stroke="#333" stroke-width="2" fill="none"/><circle cx="29" cy="11" r="1.6" fill="#333"/>
      <rect x="46" y="2" width="23" height="11" rx="3" stroke="#999" fill="none"/><rect x="48" y="4" width="5" height="7" fill="#333"/>
    </svg>

    <svg class="abs back" width="20" height="18" viewBox="0 0 20 18" aria-hidden="true"><path d="M19 9H2M9 1 1 9l8 8" stroke="#333" stroke-width="2" fill="none"/></svg>
    <span class="abs driver-name">John Smith</span>
    <span class="abs driver-license">License : 1234567890</span>
    <svg class="abs sync-ok" width="18" height="14" viewBox="0 0 18 14" aria-hidden="true"><ellipse cx="9" cy="8" rx="8" ry="5" fill="none" stroke="var(--ok)" stroke-width="2"/><path d="M5 8l3 3 6-7" stroke="var(--ok)" stroke-width="2" fill="none"/></svg>
    <span class="abs sync-btn">Sync Now</span>
    <div class="rule" style="top:116px"></div>

    <h1 class="abs page-title">Report Transfer</h1>
    <div class="rule" style="top:165px"></div>

    <span class="abs field-label" style="top:199px">Email</span>
    <span class="abs field-value email" style="top:222px">admin@roadpliant.com.au</span>
    <div class="field-line" style="top:249px"></div>

    <span class="abs field-label" style="top:272px">Email Subject</span>
    <span class="abs field-value subject" style="top:295px">Compliance Report 19/08/2023 to 25/08/2023</span>
    <div class="field-line" style="top:321px"></div>

    <span class="abs field-label" style="top:346px">Email Body</span>
    <div class="abs body-text">
      <p>Hi Mike</p>
      <p>Please find attached a PDF of my compliance report for the following dates</p>
      <p>19/08/2023 to 25/08/2023</p>
      <p>Sent by John Smith using the Roadpliant EWD</p>
    </div>
    <div class="field-line" style="top:619px"></div>
    <span class="abs count">157/300</span>

    <div class="btn btn-return">Return</div>
    <div class="btn btn-send">Send</div>
  </main>
</body>
</html>
```